TONVALE - A modern gin bottle label

Design of a bottle label in a modern fresh design. The name of the gin is "TONVALE Phantom Batch K7". Please take a look at the tonvale.de website. on the main page of tonvale.de you can breathe the design direction here: 1) the taste of the gin should be composed of 10 botanicals ... an important scent note. ) a distinctive flavor is spicy and fresh 3.) The filling volume is 0.5 liters 4.) the alcohol content is 43% vol. 5.) the variety is called "dry gin" 6.) tonvale stands for "energy" and "love"

Target Market(s)

Alcohol consumer

Colors

Designer to choose colors to be used in the design.

Requirements
Must have
• the tonvale corporate logo must be included, the name of the gin is "TONVALE Phantom Batch K7"
Nice to have
• Please use the bottles template in the appendix. (The Black Bottles) they can use the saying "DESTILLED & BOTTLED BY OLD MARINER" in small letters

```html
<!DOCTYPE html>
<html lang="en">
<head>
<meta charset="utf-8">
<title>TONVALE Phantom Batch K7 – Label</title>
<link rel="stylesheet" href="https://fonts.googleapis.com/css2?family=Russo+One&family=Metal+Mania&family=Oxanium:wght@500&family=Michroma&display=swap">
<style>
  :root {
    --bg: #121212;
    --label-black: #1b1b1b;
    --white: #f4f4f4;
    --orange: #ff6a00;
  }
  * { margin: 0; padding: 0; box-sizing: border-box; }
  html, body { width: 1200px; height: 933px; overflow: hidden; background: var(--bg); }
  .canvas {
    width: 1200px; height: 933px;
    display: flex; align-items: center; justify-content: center;
    background: var(--bg);
  }
  .label {
    width: 520px; height: 760px;
    background: var(--label-black);
    border-radius: 18px;
    display: flex; flex-direction: column; align-items: center;
    padding-top: 150px;
  }
  .brand {
    display: flex; align-items: center; gap: 12px;
    font-family: "Russo One", sans-serif;
    font-size: 40px; letter-spacing: 2px;
    color: var(--white);
  }
  .brand-mark { width: 22px; height: 22px; background: var(--orange); }
  .product-name {
    margin-top: 40px;
    font-family: "Metal Mania", cursive;
    font-size: 120px; line-height: 0.9;
    color: var(--white);
    letter-spacing: 2px;
  }
  .product-batch {
    align-self: flex-end;
    margin-right: 70px;
    margin-top: 2px;
    font-family: "Oxanium", sans-serif;
    font-weight: 500;
    font-size: 36px; letter-spacing: 1px;
    color: var(--orange);
  }
  .variety {
    margin-top: 70px;
    font-family: "Michroma", sans-serif;
    font-size: 26px; letter-spacing: 5px;
    color: var(--white);
  }
  .strength {
    margin-top: 10px;
    font-family: "Michroma", sans-serif;
    font-size: 11px; letter-spacing: 1px;
    color: var(--orange);
  }
  .volume {
    margin-top: 90px;
    font-family: "Michroma", sans-serif;
    font-size: 18px; letter-spacing: 6px;
    color: var(--white);
  }
</style>
</head>
<body>
  <main class="canvas">
    <section class="label">
      <div class="brand"><span class="brand-mark"></span><span class="brand-name">TONVALE</span></div>
      <h1 class="product-name">Phantom</h1>
      <p class="product-batch">BATCH K7</p>
      <p class="variety">DRY GIN</p>
      <p class="strength">43% VOL</p>
      <p class="volume">0.5 L</p>
    </section>
  </main>
</body>
</html>
```